Website design for Cambridge based systematic hedge fund

We have run previous craftmosaic competitions to design our company logo, business cards and the styling of our presentation deck (see attached files).
As the final step we are looking to get a website designed that is thematically consistent with these existing elements of our branding.
You can find some of our competitors websites below:
https://www.quelmarsh.example/
https://www.fenloor.example/
https://www.pyvart.example/
https://www.dulvet.example/
https://www.orbelmfunds.example/
https://www.valtrigo.example/
https://www.meskilfunds.example/home
We would like to have a website that works well on both mobile devices and desktops. Either just as one page that can be scrolled down, with links at the top that skips to certain sections, or a few separate pages that can be navigated by a top menu.
It should look professional, we are not after lots of animations or unnecessary transitions, and in particular the website must be smooth to navigate. We would like to avoid having peoples of people, we are happy to make use of elements from the presentation (for example the style of the cover slide, or the section slides with the faded bridge in the background), or 'financial' style images.
We would like to have the following sections for now. For some of these some example text has been provided, final text may change but it will be of similar length. For the other sections we are happy to just have template text for now. At the moment we are mainly interested to see styles/layouts as words can be added easily afterwards:
1) We will need a disclaimer pop up the first time someone visits the site (see for example the meskilfunds example).
2) Top page - company name, then in larger text "Bringing AI and Statistical Inference to Financial Markets", and somewhere in smaller text "Harlow Vectors is a quantitative asset manager with the singular focus of delivering algorithmic strategies that work"
3) "About us" section: will describe us as a company, details our approach, company values, and explains the company logo.
Example text:
"We deliver consistent alpha across liquid markets through the application of proprietary IP in Bayesian inference, machine learning and artificial intelligence. We are a multi-disciplinary team founded by experienced finance professionals from premier institutions, leading academics from the Thornbury Stellar Unit at Ashmere College and world-class software engineers.
Our logo portrays a sillhoute of the lattice walkway at Ashmere College. Our unique scientific approach allows us to bridge cutting-edge mathematical research and computing expertise with financial knowledge to bring algorithmns that work to liquid markets"
4) Hiring section, detailing our culture, what we are looking for.
Example text:
"We are always looking for exceptional talent to join our entrepreneurial team. We are looking for individuals who are creative thinkers, can demonstrate analytical rigour and are passionate about the intersection of science, finance and technology.
We prioritise having a company culture that promotes sharing ideas in a safe, collaborative research environment. We make sure that every member of the team has the oppertunity to explore their own ideas through weekly 'innovation time', and ensure that everyone gets the support they need to continue to grow as individuals within the company."
5) A section for news/press releases
6) Contact us area at the bottom with office location and email. We will need to list 3 addresses for our Cambridge, London and Singapore offices, along with a couple of contact emails or phone numbers
7) A client login button at the top that will take them to a different website (unrelated to this one).

```html
<!DOCTYPE html>
<html lang="en">
<head>
<meta charset="utf-8">
<title>Harlow Vectors</title>
<link href="https://fonts.googleapis.com/css2?family=Montserrat:wght@400;600;700&family=Open+Sans:wght@400;600;700&display=swap" rel="stylesheet">
<style>
:root{
  --navy:#0d1b30;
  --navy-deep:#081222;
  --blue:#2f5fd0;
  --ink:#1d2433;
  --muted:#6b7380;
  --line:#cfd4dc;
  --white:#ffffff;
  --photo-a:#3f5a3c;
  --photo-b:#8a7a5c;
  --photo-c:#2c3d4c;
}
*{box-sizing:border-box;margin:0;padding:0}
html,body{width:1200px;height:3948px;overflow:hidden}
body{font-family:"Open Sans",Arial,sans-serif;color:var(--ink);background:var(--white);position:relative}
section,header,footer{position:absolute;left:0;width:1200px}
.abs{position:absolute}
h1,h2,h3,.brand{font-family:"Montserrat",Arial,sans-serif}

/* first visit state with disclaimer */
.first-visit{top:0;height:640px;overflow:hidden}
.first-visit .hero-photo{position:absolute;inset:0;background:linear-gradient(170deg,var(--photo-c) 0%,var(--photo-a) 45%,var(--photo-b) 100%)}
.first-visit .shade{position:absolute;inset:0;background:rgba(0,0,0,.55)}
.mini-nav{position:absolute;top:30px;right:70px;display:flex;gap:20px;color:var(--white);font:600 13px "Montserrat",sans-serif;opacity:.6}
.mini-brand{position:absolute;top:24px;left:70px;color:var(--white);font:700 16px "Montserrat",sans-serif;opacity:.6}
.disclaimer{position:absolute;left:300px;top:92px;width:600px;height:496px;background:var(--white);padding:26px 36px;text-align:center;font-size:12px;line-height:1.45}
.disclaimer .brand{font-size:20px;color:var(--navy);font-weight:700;letter-spacing:1px}
.disclaimer h3{font-size:14px;margin:20px 0 10px;letter-spacing:.5px}
.disclaimer p{text-align:left}
.terms-box{border:1px solid var(--line);height:110px;margin:12px 0 18px;padding:10px;text-align:left;font-size:11px;overflow:hidden;color:#333}
.terms-box p{margin-bottom:8px}
.choices{display:flex;justify-content:center;gap:20px}
.choice{padding:7px 22px;border-radius:3px;font-size:12px;color:var(--white);background:var(--blue)}
.choice.decline{background:#8a8f98}

/* header */
.site-header{top:760px;height:80px;background:var(--navy)}
.site-header .brand{position:absolute;left:80px;top:26px;color:var(--white);font-size:20px;font-weight:700;letter-spacing:1px}
.main-nav{position:absolute;right:80px;top:31px;display:flex;gap:26px;color:var(--white);font:600 14px "Montserrat",sans-serif}

/* hero */
.hero{top:840px;height:380px;overflow:hidden}
.hero .hero-photo{position:absolute;inset:0;background:linear-gradient(175deg,#5d7a86 0%,var(--photo-a) 40%,var(--photo-b) 75%,#6e5a48 100%)}
.hero .shade{position:absolute;inset:0;background:rgba(10,20,35,.35)}
.hero h1{position:absolute;top:66px;width:100%;text-align:center;color:var(--white);font-size:32px;font-weight:600}
.hero p{position:absolute;top:128px;left:330px;width:540px;text-align:center;color:var(--white);font-size:15px;line-height:1.45}
.hero svg{position:absolute;bottom:0;left:0}

/* about */
.about{top:1220px;height:280px;text-align:center}
.about h2{font-size:28px;margin-top:0}
.about h3{font-size:15px;margin-top:10px}
.about p{width:840px;margin:12px auto 0;font-size:12px;line-height:1.5;color:var(--muted)}
.btn{display:inline-block;background:var(--blue);color:var(--white);font:600 12px "Montserrat",sans-serif;padding:9px 20px;border-radius:3px}
.about .btn{margin-top:20px}

/* section heads */
.band{background:var(--navy);color:var(--white);text-align:center}
.band h2{position:absolute;width:100%;font-size:26px;font-weight:600}
.band svg{position:absolute;left:560px}
.hiring-head{top:1500px;height:320px}
.hiring-head svg{top:160px}
.hiring-head h2{top:252px}

.hiring-body{top:1820px;height:480px;overflow:hidden}
.hiring-body .hero-photo{position:absolute;inset:0;background:linear-gradient(120deg,#2b2c33 0%,#6a5b4e 45%,#3e3b3e 100%)}
.hiring-box{position:absolute;left:180px;top:100px;width:840px;height:230px;background:rgba(0,0,0,.72);color:var(--white);padding:28px 36px;font-size:12px;line-height:1.55}
.hiring-box p{margin-bottom:10px}

.press-head{top:2300px;height:320px}
.press-head svg{top:64px}
.press-head h2{top:148px}

/* cards */
.cards{top:2540px;height:480px}
.card{position:absolute;top:0;width:280px;height:470px;background:var(--white);box-shadow:0 4px 16px rgba(0,0,0,.18)}
.card .thumb{height:200px}
.card .body{padding:18px 16px}
.card .tag{font-size:9px;font-weight:700;color:var(--muted)}
.card h3{font-size:16px;line-height:1.3;margin:6px 0 8px}
.card .date{font-size:9px;color:var(--muted)}
.card p{font-size:10px;color:var(--muted);line-height:1.45;margin:10px 0 18px}
.card .btn{border-radius:14px;padding:7px 16px;font-size:10px}

/* contact */
.contact{top:3020px;height:520px}
.contact h2{position:absolute;left:160px;top:130px;font-size:22px;color:var(--blue);line-height:1.3}
.contact .intro{position:absolute;left:160px;top:200px;width:300px;font-size:11px;color:var(--muted);line-height:1.5}
.contact .mail{position:absolute;left:160px;top:262px}
.field{position:absolute;left:680px;width:340px;font-size:12px;border-bottom:1px solid var(--ink);padding-bottom:16px}
.offices{position:absolute;left:160px;top:370px;display:flex;gap:80px}
.office{width:160px;font-size:10px;line-height:1.45;color:var(--muted)}
.office h4{font:700 10px "Montserrat",sans-serif;color:var(--blue);margin-bottom:8px}

/* footer */
.social{top:3540px;height:200px;background:var(--white)}
.social svg.wave{position:absolute;top:0;left:0}
.social-links{position:absolute;top:110px;left:0;width:100%;display:flex;justify-content:center;gap:190px}
.social-links span{width:30px;height:30px;border-radius:50%;background:var(--white)}
.site-footer{top:3740px;height:208px;background:var(--navy-deep);color:#c6ccd6}
.foot-cols{position:absolute;left:160px;top:32px;display:flex;gap:230px;font-size:11px;line-height:1.6}
.foot-cols h4{font:700 11px "Montserrat",sans-serif;color:var(--white);margin-bottom:4px}
.copyright{position:absolute;bottom:12px;width:100%;text-align:center;font-size:10px}
</style>
</head>
<body>

<section class="first-visit">
  <div class="hero-photo" role="img" aria-label="Photo of a lattice walkway over a river with college buildings"></div>
  <div class="shade"></div>
  <div class="mini-brand">Harlow Vectors</div>
  <nav class="mini-nav"><span>Home</span><span>About</span><span>Hiring</span><span>News</span><span>Contact</span></nav>
  <div class="disclaimer">
    <div class="brand">Harlow Vectors</div>
    <h3>HARLOW VECTORS</h3>
    <p>Please read these Terms of Use (the "Terms") carefully before proceeding as they explain certain restrictions imposed by law on the distribution of the information on this website – www.harlowvectors.example – and the investor portal made available therein (the "Website").</p>
    <div class="terms-box">
      <p>1. Harlow Vectors</p>
      <p>1.1 The Website is operated and owned by Harlow Vectors LTD ("HV" or the "Company"; "we", or "us") which is authorised and regulated by the Financial Conduct Authority of the United Kingdom (the "FCA") (Reference Number 000000). You can gain access to the Website only after confirming the terms below.</p>
    </div>
    <div class="choices"><span class="choice">I accept</span><span class="choice decline">I do not accept</span></div>
    <h3>COOKIES CONTROL</h3>
    <p style="text-align:center">This website uses cookies. By continuing to use this website you are giving consent to cookies being used. For information on cookies, visit our Cookie Policy.</p>
  </div>
</section>

<header class="site-header">
  <div class="brand">Harlow Vectors</div>
  <nav class="main-nav"><span>Home</span><span>About</span><span>Hiring</span><span>News</span><span>Contact</span></nav>
</header>

<section class="hero">
  <div class="hero-photo" role="img" aria-label="Photo of a lattice walkway over a river beside old college buildings"></div>
  <div class="shade"></div>
  <h1>Bringing AI and Statistical Inference to Financial Markets</h1>
  <p>Harlow Vectors is a quantitative asset manager with the singular focus of delivering algorithmic strategies that work</p>
  <svg width="1200" height="80" viewBox="0 0 1200 80"><path d="M0 60 C300 0 900 0 1200 60 L1200 80 L0 80Z" fill="#fff"/></svg>
</section>

<section class="about">
  <h2>About Us</h2>
  <h3>Harlow Vectors</h3>
  <p>We deliver consistent alpha across liquid markets through the application of proprietary IP in Bayesian inference, machine learning and artificial intelligence. We are a multi-disciplinary team founded by experienced finance professionals from premier institutions, leading academics from the Thornbury Stellar Unit at Ashmere College and world-class software engineers.</p>
  <p>Our logo portrays a sillhoute of the lattice walkway at Ashmere College. Our unique scientific approach allows us to bridge cutting-edge mathematical research and computing expertise with financial knowledge to bring algorithmns that work to liquid markets.</p>
  <span class="btn">Read More</span>
</section>

<section class="band hiring-head">
  <svg width="80" height="80" viewBox="0 0 80 80"><rect x="6" y="6" width="68" height="68" rx="6" fill="none" stroke="#fff" stroke-width="4"/><rect x="16" y="20" width="48" height="14" fill="#fff"/><rect x="16" y="40" width="48" height="6" fill="#fff"/><rect x="16" y="52" width="48" height="6" fill="#fff"/></svg>
  <h2>Hiring</h2>
</section>

<section class="hiring-body">
  <div class="hero-photo" role="img" aria-label="Photo of a desk with a laptop and financial papers"></div>
  <div class="hiring-box">
    <p>We are always looking for exceptional talent to join our entrepreneurial team. We are looking for individuals who are creative thinkers, can demonstrate analytical rigour and are passionate about the intersection of science, finance and technology.</p>
    <p>We prioritise having a company culture that promotes sharing ideas in a safe, collaborative research environment. We make sure that every member of the team has the oppertunity to explore their own ideas through weekly 'innovation time', and ensure that everyone gets the support they need to continue to grow as individuals within the company.</p>
    <span class="btn">Read More</span>
  </div>
</section>

<section class="band press-head">
  <svg width="80" height="80" viewBox="0 0 80 80"><rect x="14" y="8" width="58" height="64" rx="4" fill="none" stroke="#fff" stroke-width="4"/><path d="M14 24 H6 V64 a8 8 0 0 0 8 8" fill="none" stroke="#fff" stroke-width="4"/><rect x="24" y="18" width="38" height="14" fill="#fff"/><rect x="24" y="40" width="38" height="5" fill="#fff"/><rect x="24" y="52" width="38" height="5" fill="#fff"/></svg>
  <h2>Press Releases</h2>
</section>

<section class="cards">
  <article class="card" style="left:132px">
    <div class="thumb" role="img" aria-label="Photo of a tablet showing a news page" style="background:linear-gradient(135deg,#c9c4bb,#6f6a62)"></div>
    <div class="body">
      <div class="tag">NEWS DESC</div>
      <h3>Make your website with best visual web designer.</h3>
      <div class="date">SEPT 01, 2017</div>
      <p>Lorem ipsum dolor sit amet, consectetur adipiscing elit. Integer nec odio. Praesent libero. Sed cursus ante dapibus diam.</p>
      <span class="btn">READ MORE</span>
    </div>
  </article>
  <article class="card" style="left:460px">
    <div class="thumb" role="img" aria-label="Photo of folded newspapers" style="background:linear-gradient(135deg,#d8d5cf,#7a7874)"></div>
    <div class="body">
      <div class="tag">NEWS DESC</div>
      <h3>Make your website with best visual web designer.</h3>
      <div class="date">SEPT 01, 2017</div>
      <p>Lorem ipsum dolor sit amet, consectetur adipiscing elit. Integer nec odio. Praesent libero. Sed cursus ante dapibus diam.</p>
      <span class="btn">READ MORE</span>
    </div>
  </article>
  <article class="card" style="left:788px">
    <div class="thumb" role="img" aria-label="Close photo of printed newspaper text" style="background:linear-gradient(135deg,#e2ddd2,#8f887b)"></div>
    <div class="body">
      <div class="tag">NEWS DESC</div>
      <h3>Make your website with best visual web designer.</h3>
      <div class="date">SEPT 01, 2017</div>
      <p>Lorem ipsum dolor sit amet, consectetur adipiscing elit. Integer nec odio. Praesent libero. Sed cursus ante dapibus diam.</p>
      <span class="btn">READ MORE</span>
    </div>
  </article>
</section>

<section class="contact">
  <h2>Any questions?<br>Feel free to contact us.</h2>
  <p class="intro">Lorem ipsum dolor sit amet, consectetur adipiscing elit. Integer nec odio. Praesent libero. Sed cursus ante dapibus diam. Sed nisi. Nulla quis sem at nibh.</p>
  <svg class="mail" width="46" height="34" viewBox="0 0 46 34"><rect x="2" y="2" width="42" height="30" rx="2" fill="none" stroke="#2f5fd0" stroke-width="3"/><path d="M3 4 L23 19 L43 4" fill="none" stroke="#2f5fd0" stroke-width="3"/></svg>
  <div class="field" style="top:40px">Name</div>
  <div class="field" style="top:108px">Email</div>
  <div class="field" style="top:188px;padding-bottom:90px">Message</div>
  <span class="btn abs" style="left:680px;top:324px;border-radius:14px;padding:7px 18px">SEND</span>
  <div class="offices">
    <div class="office"><h4>CAMBRIDGE</h4>Address:<br>12 Fenway Court Street<br>Riverside Tower, CB0 0AA<br>Phone:<br>+44 0000 000000<br>Email:<br>hello@harlowvectors.example</div>
    <div class="office"><h4>LONDON</h4>Address:<br>48 Meridian Row Street<br>Quayside House, EC0 0AA<br>Phone:<br>+44 0000 000001<br>Email:<br>london@harlowvectors.example</div>
    <div class="office"><h4>SINGAPORE</h4>Address:<br>7 Harbour Link Road<br>Marina Point, 000000<br>Phone:<br>+65 0000 0000<br>Email:<br>asia@harlowvectors.example</div>
  </div>
</section>

<section class="social">
  <svg class="wave" width="1200" height="200" viewBox="0 0 1200 200"><path d="M0 40 C300 0 900 0 1200 40 L1200 200 L0 200Z" fill="#0d1b30"/></svg>
  <div class="social-links" aria-label="Social links"><span></span><span></span><span></span><span></span></div>
</section>

<footer class="site-footer">
  <div class="foot-cols">
    <div><h4>NAVIGATE</h4>Home<br>About<br>Hiring<br>News</div>
    <div><h4>CONNECT</h4>Linkboard<br>Picturely<br>Chirper<br>Streamtube</div>
    <div><h4>MORE LINKS</h4>Client Login<br>Terms of Use<br>Cookie Policy<br>Privacy Notice</div>
  </div>
  <div class="copyright">Copyright © 2021 Harlow Vectors · All Rights Reserved</div>
</footer>

</body>
</html>
```